Bright Harbor Solar Company Letter Head

We need a clean, branded letterhead built with our company logo. We uploaded some of our promotional marketing material to show you what style we like.

Industry/Entity Type

It Company

Font styles to use
Serif
Sans Serif

Requirements
Must have
• Company Name: Bright Harbor Solar
• Contractors License Number RBQC: 2748315
• Address: 5216 Marlowe Blvd #340 Sacramento, CA 95834
• Phone Number: 916-738-2097
• Fax Number: 916-738-2097

```html
<!DOCTYPE html>
<html lang="en">
<head>
<meta charset="UTF-8">
<title>Bright Harbor Solar Letterhead</title>
<link href="https://fonts.googleapis.com/css2?family=Poppins:wght@500;600;700&display=swap" rel="stylesheet">
<style>
  :root {
    --brand-orange: #f0621c;
    --brand-orange-light: #f58a4f;
    --watermark: #fbe6d9;
    --paper: #ffffff;
    --ink-white: #ffffff;
    --ink-dark: #3a3a3a;
  }
  * { margin: 0; padding: 0; box-sizing: border-box; }
  html, body { width: 849px; height: 1200px; overflow: hidden; background: var(--paper); }
  .letterhead {
    position: relative;
    width: 849px;
    height: 1200px;
    background: var(--paper);
    font-family: "Poppins", sans-serif;
  }
  .brand {
    position: absolute;
    top: 22px;
    left: 34px;
    display: flex;
    align-items: center;
    gap: 12px;
  }
  .brand-mark {
    width: 44px;
    height: 44px;
    background: var(--brand-orange);
  }
  .brand-name {
    font-weight: 700;
    font-size: 28px;
    line-height: 1.05;
    color: var(--brand-orange);
    width: 170px;
  }
  .watermark {
    position: absolute;
    left: 272px;
    top: 300px;
    width: 306px;
    height: 306px;
    background: var(--watermark);
  }
  .footer {
    position: absolute;
    left: 0;
    bottom: 0;
    width: 849px;
    height: 104px;
  }
  .footer-band { position: absolute; inset: 0; }
  .contact {
    position: absolute;
    left: 22px;
    top: 18px;
    color: var(--ink-white);
    font-weight: 500;
    font-size: 14px;
    line-height: 23px;
  }
  .contact-row { display: flex; align-items: center; gap: 7px; }
  .contact-row svg { width: 13px; height: 13px; fill: var(--ink-white); }
  .contact-row .gap { width: 22px; }
  .license { font-weight: 600; }
  .partner {
    position: absolute;
    right: 40px;
    top: 36px;
    display: flex;
    align-items: center;
    gap: 10px;
  }
  .partner-mark {
    width: 34px;
    height: 34px;
    border-radius: 50%;
    background: var(--brand-orange);
  }
  .partner-name {
    font-weight: 600;
    font-size: 22px;
    color: var(--ink-dark);
  }
</style>
</head>
<body>
<div class="letterhead">
  <header class="brand">
    <div class="brand-mark"></div>
    <div class="brand-name">Bright Harbor Solar</div>
  </header>

  <div class="watermark" role="img" aria-label="Faint brand emblem decoration"></div>

  <footer class="footer">
    <svg class="footer-band" viewBox="0 0 849 104" preserveAspectRatio="none">
      <rect x="0" y="0" width="849" height="104" fill="var(--brand-orange)"/>
      <rect x="0" y="0" width="849" height="6" fill="var(--brand-orange-light)"/>
      <polygon points="620,18 849,18 849,104 584,104" fill="var(--paper)"/>
    </svg>
    <div class="contact">
      <div class="contact-row">
        <svg viewBox="0 0 24 24"><path d="M12 3 2 12h3v9h5v-6h4v6h5v-9h3z"/></svg>
        <span>5216 Marlowe Blvd #340 Sacramento, CA 95834</span>
      </div>
      <div class="contact-row">
        <svg viewBox="0 0 24 24"><path d="M6.6 10.8a15 15 0 0 0 6.6 6.6l2.2-2.2c.3-.3.7-.4 1-.2 1.1.4 2.3.6 3.6.6.6 0 1 .4 1 1V20c0 .6-.4 1-1 1A17 17 0 0 1 3 4c0-.6.4-1 1-1h3.5c.6 0 1 .4 1 1 0 1.3.2 2.5.6 3.6.1.3 0 .7-.2 1z"/></svg>
        <span>916-738-2097</span>
        <span class="gap"></span>
        <svg viewBox="0 0 24 24"><path d="M6 3h10v5H6zM3 9h18v10h-3v2H6v-2H3zm5 7v3h8v-3z"/></svg>
        <span>916-738-2097</span>
      </div>
      <div class="contact-row license">Contractors License Number RBQC: 2748315</div>
    </div>
    <div class="partner">
      <div class="partner-mark"></div>
      <div class="partner-name">Solstice Grid</div>
    </div>
  </footer>
</div>
</body>
</html>
```